Flyer Advertisement Design for exotic rental company

Design an advertisement for a exotic rental company:

https://zoomvela.com/

Here is a similar business:

https://www.gildmarquerides.com/

I rent out a vehicle called a Tundrix Whipcraft. Here is a link to the manufacturer website:

https://whipcraft.tundrix.com/en-us/

I have the 2018 Tundrix Whipcraft GT in the colors Navy Blue and Sunset Red

This advertisement will be printed on a flyer and placed in strategic locations to attract customers. I am looking for something that will draw the customer in. Please use your imagination and come up with something awesome!

Target Market(s)

Outgoing individuals looking to have some fun! This advertisement will be placed in a country club

Industry/Entity Type

Rental Car

Font styles to use
Serif
Sans Serif
Decorative
Script

Colors

Designer to choose colors to be used in the design.

Requirements
Must have
• Pictures of the Tundrix Whipcraft, website info, message about discount to Hollowbrook Country Club Members, phone number, anything else you feel will make the advertisement look great
Nice to have
• Anything you suggest in your professional capacity
Should not have
• Anything goes!

```html
<!DOCTYPE html>
<html lang="en">
<head>
<meta charset="utf-8">
<title>Zoomvela Exotic Car Rentals Flyer</title>
<link href="https://fonts.googleapis.com/css2?family=EB+Garamond:wght@400;500&family=Oswald:wght@600;700&display=swap" rel="stylesheet">
<style>
  :root {
    --ink: #050505;
    --charcoal: #2a2a2c;
    --white: #ffffff;
    --soft-white: #e8e8e8;
    --racing-red: #e0262b;
    --deep-red: #8e0f14;
    --page: #ffffff;
  }
  * { margin: 0; padding: 0; box-sizing: border-box; }
  html, body {
    width: 1200px;
    height: 800px;
    overflow: hidden;
    background: var(--page);
  }
  .flyer {
    position: relative;
    width: 1200px;
    height: 800px;
    overflow: hidden;
    background:
      radial-gradient(ellipse 70% 60% at 55% 30%, var(--charcoal) 0%, #141415 55%, var(--ink) 100%);
    font-family: "EB Garamond", "Times New Roman", serif;
    color: var(--white);
  }
  .vehicle-photo {
    position: absolute;
    left: 0;
    top: 0;
    width: 400px;
    height: 380px;
    background:
      radial-gradient(ellipse 55% 45% at 48% 45%, #c1161c 0%, #7a0c10 45%, rgba(20,20,21,0) 80%);
  }
  .headline-block {
    position: absolute;
    left: 40px;
    top: 400px;
  }
  .tagline {
    font-size: 46px;
    font-weight: 400;
    line-height: 1.1;
    letter-spacing: 0.2px;
  }
  .website {
    margin-top: 14px;
    font-size: 22px;
    color: var(--soft-white);
  }
  .phone {
    font-size: 30px;
    margin-top: 2px;
  }
  .member-offer {
    position: absolute;
    left: 40px;
    top: 620px;
    font-size: 17px;
    line-height: 1.3;
    color: var(--soft-white);
  }
  .racing-stripes {
    position: absolute;
    left: 0;
    top: 0;
  }
  .slogan {
    position: absolute;
    left: 520px;
    top: 560px;
    font-family: "Oswald", "Arial Narrow", sans-serif;
    font-weight: 700;
    font-size: 52px;
    letter-spacing: 0.5px;
    white-space: nowrap;
    color: var(--white);
    transform-origin: left bottom;
    transform: rotate(-14.5deg) skewX(-10deg);
  }
  .footer-url {
    position: absolute;
    right: 40px;
    bottom: 30px;
    font-size: 22px;
    color: var(--white);
  }
</style>
</head>
<body>
  <main class="flyer">
    <div class="vehicle-photo" role="img" aria-label="Front view of a red Tundrix Whipcraft GT three-wheel roadster"></div>

    <section class="headline-block">
      <h1 class="tagline">Exotic car rentals</h1>
      <p class="website">www.zoomvela.com</p>
      <p class="phone">555-014-2277</p>
    </section>

    <p class="member-offer">
      20% Off for all Hollowbrook Country<br>
      Club Members<br>
      www.zoomvela.com/HollowbrookCC
    </p>

    <svg class="racing-stripes" width="1200" height="800" viewBox="0 0 1200 800" aria-hidden="true">
      <polygon points="560,650 1200,478 1200,500 566,672" fill="var(--racing-red)"/>
      <polygon points="590,706 1200,542 1200,580 600,744" fill="var(--racing-red)"/>
      <polygon points="700,760 1200,626 1200,650 708,784" fill="var(--racing-red)"/>
    </svg>

    <p class="slogan">Earn your racing stripes</p>

    <p class="footer-url">www.zoomvela.com</p>
  </main>
</body>
</html>
```